Tamkor, a service provider dedicated to improving the performance of a website

Tamkor offers optimization and performance improvement for all types of websites (showcase sites, e-commerce, ...), with the aim of improving their ranking on Vintrel and their customer transformation rate. The main benefits consist in optimizing the factors of a site. In addition, we also offer content creation (description of product sheets, services, ...), Vintrel Ads campaign management, migration version for Prestashop / Wordpress, etc. The design must be a fresh image, dynamic, why not "fun", but also serious. No favorite color, carte blanche on this point;)

```html
<!DOCTYPE html>
<html lang="en">
<head>
<meta charset="utf-8">
<title>Tamkor — Business Cards</title>
<link rel="stylesheet" href="https://fonts.googleapis.com/css2?family=Lato:wght@400;700;900&display=swap">
<style>
  :root {
    --stage: #2b2b2b;
    --brand-blue: #3b57a4;
    --deep-blue: #1c4b8e;
    --paper: #ffffff;
    --ink-green: #2f4a24;
    --back-text: #c9cce6;
  }
  * { margin: 0; padding: 0; box-sizing: border-box; }
  html, body {
    width: 1200px; height: 878px; overflow: hidden;
    background: var(--stage);
    font-family: "Lato", Arial, sans-serif;
  }
  .stage { position: relative; width: 1200px; height: 878px; }
  .card {
    position: absolute; top: 284px;
    width: 540px; height: 310px;
    overflow: hidden;
  }
  .card-back {
    left: 620px;
    background: var(--brand-blue);
    display: flex; align-items: center; justify-content: center;
  }
  .card-back .wordmark {
    font-weight: 900; font-size: 96px; letter-spacing: -2px;
    color: var(--back-text);
  }
  .card-front { left: 40px; background: var(--paper); }
  .card-front .corner { position: absolute; inset: 0; }
  .card-front .wordmark {
    position: absolute; left: 34px; top: 22px;
    font-weight: 900; font-size: 64px; letter-spacing: -1.5px;
    color: var(--brand-blue);
  }
  .holder { position: absolute; left: 38px; top: 122px; }
  .holder .name {
    font-weight: 900; font-size: 26px; color: var(--brand-blue);
    letter-spacing: 0.5px;
  }
  .holder .role { font-size: 16px; color: var(--ink-green); margin-top: 1px; }
  .address {
    position: absolute; left: 38px; top: 186px;
    font-size: 16px; line-height: 21px; color: var(--ink-green);
  }
  .contacts {
    position: absolute; left: 34px; top: 234px;
    list-style: none; font-size: 16px; line-height: 22px; color: var(--ink-green);
  }
  .contacts li { display: flex; align-items: center; gap: 10px; }
  .contacts svg { width: 14px; height: 14px; fill: var(--brand-blue); flex: none; }
</style>
</head>
<body>
<main class="stage">
  <section class="card card-front">
    <svg class="corner" viewBox="0 0 540 310" aria-hidden="true">
      <polygon points="540,0 540,310 380,310" fill="var(--deep-blue)"/>
    </svg>
    <div class="wordmark">Tamkor</div>
    <div class="holder">
      <div class="name">ELIAS MARTEN</div>
      <div class="role">Founder &amp; CEO</div>
    </div>
    <div class="address">
      <div>1234 First Line Address</div>
      <div>5678 Second Line Address</div>
    </div>
    <ul class="contacts">
      <li>
        <svg viewBox="0 0 24 24"><path d="M6.6 10.8a15 15 0 0 0 6.6 6.6l2.2-2.2c.3-.3.7-.4 1-.2 1.1.4 2.3.6 3.6.6.6 0 1 .4 1 1V20c0 .6-.4 1-1 1A17 17 0 0 1 3 4c0-.6.4-1 1-1h3.5c.6 0 1 .4 1 1 0 1.3.2 2.5.6 3.6.1.3 0 .7-.2 1z"/></svg>
        1234567890
      </li>
      <li>
        <svg viewBox="0 0 24 24"><path d="M2 5h20v14H2z M2 5l10 8 10-8" stroke="#fff" stroke-width="1.5"/></svg>
        info@yourmail.com
      </li>
      <li>
        <svg viewBox="0 0 24 24"><circle cx="12" cy="12" r="10"/><path d="M2 12h20M12 2c3 3 3 17 0 20M12 2c-3 3-3 17 0 20" stroke="#fff" stroke-width="1.2" fill="none"/></svg>
        www.yourwebsite.com
      </li>
    </ul>
  </section>

  <section class="card card-back">
    <div class="wordmark">Tamkor</div>
  </section>
</main>
</body>
</html>
```